Robotic consulting firm needs a Powerpoint Template

I'm looking for a powerpoint template for my consulting business. We are in the robotic field and needs to present project concept or robotic cell layout to the client. I'm looking for a design that is professionnal and using my logo. Our color is purple, but I don't want to overuse the color everywhere, it needs to look professionnal for the engineer field. Color code is 9F35D8

```html
<!DOCTYPE html>
<html lang="en">
<head>
<meta charset="utf-8">
<title>Novarch — Presentation Template</title>
<link href="https://fonts.googleapis.com/css2?family=Lato:wght@400;700&display=swap" rel="stylesheet">
<style>
:root{
  --purple:#9f35d8;
  --purple-deep:#8a2bc4;
  --ink:#222222;
  --text:#555555;
  --muted:#8a8a8a;
  --line:#cfcfcf;
  --blue:#1f6fb8;
  --white:#ffffff;
}
*{box-sizing:border-box;margin:0;padding:0}
html,body{width:1031px;height:1200px;overflow:hidden;background:var(--white);font-family:'Lato',sans-serif;color:var(--ink)}
.slide{position:absolute;width:454px;height:255px;background:var(--white);box-shadow:0 1px 4px rgba(0,0,0,.28);overflow:hidden}
.slide--cover{background:linear-gradient(160deg,#9a33d4 0%,#8f30cc 60%,#9b38d6 100%);color:var(--white)}
.footer{position:absolute;left:0;bottom:0;width:100%;height:16px;background:var(--purple);color:var(--white);font-size:5.5px;display:flex;align-items:center;justify-content:space-between;padding:0 12px}
.slide--cover .footer{background:transparent}
.abs{position:absolute}
.brand-mark{position:absolute;background:var(--purple)}
.slide--cover .brand-mark{background:var(--white)}
.wordmark{position:absolute;font-weight:700;letter-spacing:.22em;color:var(--purple);white-space:nowrap}
.slide--cover .wordmark{color:var(--white)}
.title{position:absolute;font-weight:700;color:var(--ink);white-space:nowrap}
.center{left:0;width:100%;text-align:center}
.para{position:absolute;font-size:6.3px;line-height:9px;color:var(--text)}
.tiny{font-size:3.6px;line-height:5px;color:var(--text);text-align:center}
svg text{font-family:'Lato',sans-serif}
/* services */
.card{position:absolute;top:102px;width:99px;height:114px;border:1.5px solid #e6e6e6;border-radius:5px;background:var(--white)}
.card--active{background:var(--purple);border-color:var(--purple);color:var(--white)}
.card__icon{position:absolute;left:10px;top:15px;width:26px;height:26px;background:#f0f0f0;border-radius:2px;display:flex;align-items:center;justify-content:center}
.card--active .card__icon{background:rgba(255,255,255,.25)}
.card__label{position:absolute;left:10px;top:60px;font-size:7px;border-left:1.5px solid var(--purple);padding-left:4px}
.card--active .card__label{border-color:var(--white)}
.card__text{position:absolute;left:10px;top:76px;width:80px;font-size:5.6px;line-height:8.8px;color:var(--muted)}
.card--active .card__text{color:var(--white)}
/* list */
.list-row{position:absolute;width:156px;height:14px;border-bottom:1px solid #9a9a9a;display:flex;justify-content:space-between;font-size:6.8px;font-weight:700}
.list-row--accent{color:var(--purple);border-color:#c89be6}
/* how it works */
.step{position:absolute;width:80px;text-align:center}
.step__title{font-size:7px;color:var(--purple);font-weight:700;margin-bottom:2px}
.step__text{font-size:4.3px;line-height:6.8px;color:var(--muted)}
</style>
</head>
<body>

<!-- Slide 01: cover -->
<section class="slide slide--cover" style="left:35px;top:39px">
  <div class="brand-mark" style="left:207px;top:24px;width:40px;height:40px"></div>
  <div class="wordmark center" style="top:101px;font-size:16px;padding-left:.22em">NOVARCH</div>
  <div class="abs center" style="top:134px;font-size:13px">Welcome to</div>
  <div class="abs center" style="top:153px;font-size:35px;font-weight:700">NOVARCH</div>
  <div class="abs center" style="top:197px;font-size:6.6px;line-height:9.5px">Excepteur sint occaecat cupidatat non proident, sunt in culpa<br>deserunt mollit anim id est laborum.</div>
  <footer class="footer"><span>05/09/2024</span><span>Copyright © 2024 Novarch. All rights reserved.</span><span>Page: 01</span></footer>
</section>

<!-- Slide 05: what we do -->
<section class="slide" style="left:534px;top:39px">
  <div class="title center" style="top:37px;font-size:16px">What We Do</div>
  <div class="brand-mark" style="left:396px;top:12px;width:30px;height:30px"></div>
  <div class="wordmark" style="left:373px;top:60px;font-size:9.5px">NOVARCH</div>
  <svg class="abs" style="left:0;top:0" width="454" height="255" viewBox="0 0 454 255">
    <g stroke-width="5" stroke-linecap="round">
      <line x1="28" y1="145" x2="93" y2="145" stroke="#9f35d8"/>
      <line x1="93" y1="145" x2="160" y2="145" stroke="#222"/>
      <line x1="160" y1="145" x2="226" y2="145" stroke="#9f35d8"/>
      <line x1="226" y1="145" x2="293" y2="145" stroke="#222"/>
      <line x1="293" y1="145" x2="359" y2="145" stroke="#9f35d8"/>
      <line x1="359" y1="145" x2="427" y2="145" stroke="#222"/>
    </g>
    <g fill="none" stroke-width="1.6">
      <g stroke="#9f35d8"><line x1="60" y1="113" x2="60" y2="150"/><circle cx="60" cy="100" r="12.5" fill="#fff"/></g>
      <g stroke="#9f35d8"><line x1="193" y1="113" x2="193" y2="150"/><circle cx="193" cy="100" r="12.5" fill="#fff"/></g>
      <g stroke="#1f6fb8"><line x1="327" y1="113" x2="327" y2="150"/><circle cx="327" cy="100" r="12.5" fill="#fff"/></g>
      <g stroke="#222"><line x1="126" y1="140" x2="126" y2="177"/><circle cx="126" cy="190" r="12.5" fill="#fff"/></g>
      <g stroke="#222"><line x1="259" y1="140" x2="259" y2="177"/><circle cx="259" cy="190" r="12.5" fill="#fff"/></g>
      <g stroke="#222"><line x1="394" y1="140" x2="394" y2="177"/><circle cx="394" cy="190" r="12.5" fill="#fff"/></g>
    </g>
    <g fill="#9f35d8"><path d="M56 150 L64 150 L60 155Z"/><path d="M189 150 L197 150 L193 155Z"/><path d="M323 150 L331 150 L327 155Z"/></g>
    <g fill="#222"><path d="M122 140 L130 140 L126 135Z"/><path d="M255 140 L263 140 L259 135Z"/><path d="M390 140 L398 140 L394 135Z"/></g>
    <g font-size="8" text-anchor="middle">
      <text x="60" y="103" fill="#9f35d8">01</text><text x="193" y="103" fill="#9f35d8">03</text><text x="327" y="103" fill="#1f6fb8">05</text>
      <text x="126" y="193" fill="#222" font-weight="700">02</text><text x="259" y="193" fill="#222" font-weight="700">04</text><text x="394" y="193" fill="#222" font-weight="700">06</text>
    </g>
    <g font-size="6.6" text-anchor="middle">
      <text x="126" y="97" fill="#222">Novarch 2</text><text x="259" y="97" fill="#222">Novarch 4</text><text x="394" y="97" fill="#222">Novarch 6</text>
      <text x="60" y="168" fill="#9f35d8">Novarch 1</text><text x="193" y="168" fill="#9f35d8">Novarch 3</text><text x="327" y="168" fill="#9f35d8">Novarch 5</text>
    </g>
    <g font-size="3.6" fill="#666" text-anchor="middle">
      <g transform="translate(126 104)"><text>Excepteur sint occaecat cupi-</text><text y="7">datat non proident, sunt in culpa</text><text y="14">qui officia deserunt mollit anim</text><text y="21">id est laborum.</text></g>
      <g transform="translate(259 104)"><text>Excepteur sint occaecat cupi-</text><text y="7">datat non proident, sunt in culpa</text><text y="14">qui officia deserunt mollit anim</text><text y="21">id est laborum.</text></g>
      <g transform="translate(394 104)"><text>Excepteur sint occaecat cupi-</text><text y="7">datat non proident, sunt in culpa</text><text y="14">qui officia deserunt mollit anim</text><text y="21">id est laborum.</text></g>
      <g transform="translate(60 175)"><text>Excepteur sint occaecat cupi-</text><text y="7">datat non proident, sunt in culpa</text><text y="14">qui officia deserunt mollit anim</text><text y="21">id est laborum.</text></g>
      <g transform="translate(193 175)"><text>Excepteur sint occaecat cupi-</text><text y="7">datat non proident, sunt in culpa</text><text y="14">qui officia deserunt mollit anim</text><text y="21">id est laborum.</text></g>
      <g transform="translate(327 175)"><text>Excepteur sint occaecat cupi-</text><text y="7">datat non proident, sunt in culpa</text><text y="14">qui officia deserunt mollit anim</text><text y="21">id est laborum.</text></g>
    </g>
  </svg>
  <footer class="footer"><span>05/09/2024</span><span>Copyright © 2024 Novarch. All rights reserved.</span><span>Page: 05</span></footer>
</section>

<!-- Slide 02: about us -->
<section class="slide" style="left:34px;top:329px">
  <svg class="abs" style="left:14px;top:16px" width="176" height="201" viewBox="0 0 176 201" role="img" aria-label="Photo of a hand touching a glowing robot assistant interface">
    <defs><linearGradient id="aboutPhoto" x1="0" y1="0" x2="1" y2="1"><stop offset="0" stop-color="#1c2b44"/><stop offset=".55" stop-color="#0e3b5c"/><stop offset="1" stop-color="#4a3a3a"/></linearGradient></defs>
    <polygon points="88,0 176,50 176,151 88,201 0,151 0,50" fill="url(#aboutPhoto)"/>
  </svg>
  <div class="title" style="left:217px;top:52px;font-size:16px">About Us</div>
  <div class="brand-mark" style="left:390px;top:10px;width:30px;height:30px"></div>
  <div class="wordmark" style="left:368px;top:58px;font-size:9.5px">NOVARCH</div>
  <p class="para" style="left:215px;top:83px;width:225px">Lorem ipsum dolor sit amet, consectetur adipiscing elit, sed do eiusmod tempor incididunt ut labore et dolore magna aliqua. Ut enim ad minim veniam, quis nostrud exercitation ullamco laboris nisi ut aliquip ex ea commodo consequat. Duis aute irure dolor in reprehenderit in voluptate velit esse cillum dolore eu fugiat nulla pariatur. Excepteur sint occaecat cupidatat non proident, sunt in culpa qui officia deserunt mollit anim id est laborum.</p>
  <p class="para" style="left:215px;top:156px;width:228px">Sed ut perspiciatis unde omnis iste natus error sit voluptatem accusantium doloremque laudantium, totam rem aperiam, eaque ipsa quae ab illo ven tore veritatis et quasi architecto beatae vitae dicta sunt explicabo. Nemo enim ipsam voluptatem quia voluptas sit aspernatur aut odit aut fugit, sed quia consequuntur magni dolores eos qui ratione voluptatem sequi Ut enim ad minima veniam, quis nostrum exercitationem ullam adipisci velit, sed quia non numquam eiusnesciunt.</p>
  <footer class="footer"><span>05/09/2024</span><span>Copyright © 2024 Novarch. All rights reserved.</span><span>Page: 02</span></footer>
</section>

<!-- Slide 06: our process -->
<section class="slide" style="left:534px;top:331px">
  <svg class="abs" style="left:0;top:0" width="300" height="240" viewBox="0 0 300 240">
    <g font-size="5.5" text-anchor="middle">
      <rect x="22" y="38" width="33" height="156" fill="#9f35d8"/><text x="38.5" y="33" fill="#9f35d8">95%</text>
      <rect x="62" y="63" width="33" height="131" fill="#262626"/><text x="78.5" y="58" fill="#222">80%</text>
      <rect x="102" y="116" width="33" height="78" fill="#9f35d8"/><text x="118.5" y="111" fill="#9f35d8">60%</text>
      <rect x="142" y="138" width="33" height="56" fill="#262626"/><text x="158.5" y="133" fill="#222">45%</text>
      <rect x="182" y="134" width="33" height="60" fill="#9f35d8"/><text x="198.5" y="129" fill="#9f35d8">50%</text>
      <rect x="222" y="146" width="33" height="48" fill="#262626"/><text x="238.5" y="141" fill="#222">40%</text>
      <rect x="262" y="157" width="33" height="37" fill="#9f35d8"/><text x="278.5" y="152" fill="#9f35d8">30%</text>
    </g>
    <g font-size="5.6" text-anchor="middle">
      <text x="38.5" y="204" fill="#9f35d8">Lorem</text><text x="38.5" y="212" fill="#9f35d8">Ipsum</text>
      <text x="78.5" y="204" fill="#222">Finibus</text><text x="78.5" y="212" fill="#222">Bonorum</text>
      <text x="118.5" y="204" fill="#9f35d8">Nemo enim</text><text x="118.5" y="212" fill="#9f35d8">ipsam</text>
      <text x="158.5" y="204" fill="#222">Sed ut</text><text x="158.5" y="212" fill="#222">perspiciatis</text>
      <text x="198.5" y="204" fill="#9f35d8">Ut enim ad</text><text x="198.5" y="212" fill="#9f35d8">minima</text>
      <text x="238.5" y="204" fill="#222">Excepteur</text><text x="238.5" y="212" fill="#222">sint</text>
      <text x="278.5" y="204" fill="#9f35d8">Duis aute</text><text x="278.5" y="212" fill="#9f35d8">irure</text>
    </g>
  </svg>
  <svg class="abs" style="left:300px;top:0" width="60" height="240" viewBox="0 0 60 240">
    <rect x="2" y="178" width="33" height="16" fill="#262626"/>
    <text x="18.5" y="173" font-size="5.5" text-anchor="middle" fill="#222">10%</text>
    <text x="18.5" y="204" font-size="5.6" text-anchor="middle" fill="#777">Ut enim ad</text>
    <text x="18.5" y="212" font-size="5.6" text-anchor="middle" fill="#777">minim</text>
  </svg>
  <div class="title" style="left:174px;top:34px;font-size:16px">Our Process</div>
  <p class="para" style="left:174px;top:63px;width:265px">Sed ut perspiciatis unde omnis iste natus error sit voluptatem accusantium dolorem que laudantium, totam rem ape riam, eaque ipsa quae ab illo inventore veritatis et quasi architecto beatae vitae dicta sunt explicabo. Nemo enim ipsam voluptatem quia voluptas sit aspernatur aut odit aut fugit, d nesciunt.</p>
  <footer class="footer"><span>05/09/2024</span><span>Copyright © 2024 Novarch. All rights reserved.</span><span>Page: 06</span></footer>
</section>

<!-- Slide 03: our services -->
<section class="slide" style="left:35px;top:616px">
  <div class="title center" style="top:32px;font-size:16px">Our Services</div>
  <p class="para center" style="top:58px;padding:0 48px;text-align:center">Sed ut perspiciatis unde omnis iste natus error sit voluptatem accusantium doloremque laudantium, totam rem ape riam, eaque ipsa quae ab illo inventore veritatis et quasi architecto beatae vitae dicta sunt explicabo. Nemo enim ipsam voluptatem quia voluptas sit aspernatur aut odit aut fugit, d nesciunt.</p>

  <div class="card" style="left:14px">
    <div class="card__icon"><svg width="14" height="14" viewBox="0 0 14 14"><circle cx="7" cy="6" r="4.5" fill="none" stroke="#9f35d8" stroke-width="1.4"/><circle cx="7" cy="6" r="1.8" fill="#9f35d8"/><path d="M4.5 10 L3.5 13.5 L7 12 L10.5 13.5 L9.5 10" fill="#9f35d8"/></svg></div>
    <div class="card__label">Novarch 1</div>
    <p class="card__text">Excepteur sint occaecat cupidatat non proident, sunt mollit anim id est laborum.</p>
  </div>
  <div class="card" style="left:124px">
    <div class="card__icon"><svg width="14" height="14" viewBox="0 0 14 14"><circle cx="5" cy="8.5" r="4" fill="#9f35d8"/><rect x="7" y="1" width="6.5" height="5" rx="1" fill="none" stroke="#9f35d8" stroke-width="1"/><text x="5" y="10.5" font-size="5" text-anchor="middle" fill="#fff">?</text></svg></div>
    <div class="card__label">Novarch 2</div>
    <p class="card__text">Excepteur sint occaecat cupidatat non proident, sunt mollit anim id est laborum.</p>
  </div>
  <div class="card card--active" style="left:234px">
    <div class="card__icon"><svg width="16" height="12" viewBox="0 0 16 12"><path d="M1 4 L5 2 L8 4 L11 2 L15 4 L12 9 L8 11 L4 9Z" fill="#fff"/></svg></div>
    <div class="card__label">Novarch 3</div>
    <p class="card__text">Excepteur sint occaecat sunt in culpa qui deserunt mollit anim id est laborum.</p>
  </div>
  <div class="card" style="left:343px">
    <div class="card__icon"><svg width="14" height="14" viewBox="0 0 14 14"><circle cx="8" cy="4.5" r="3" fill="none" stroke="#9f35d8" stroke-width="1.6"/><path d="M1 9 L5 9 L8 10.5 L13 8.5 L13 10 L8 13 L1 12Z" fill="#9f35d8"/></svg></div>
    <div class="card__label">Novarch 4</div>
    <p class="card__text">Excepteur sint occaecat cupidatat non proident, sunt mollit anim id est laborum.</p>
  </div>
  <footer class="footer"><span>05/09/2024</span><span>Copyright © 2024 Novarch. All rights reserved.</span><span>Page: 03</span></footer>
</section>

<!-- Slide 07: how it works -->
<section class="slide" style="left:534px;top:617px">
  <div class="title center" style="top:27px;font-size:16px">How It Works</div>
  <svg class="abs" style="left:0;top:0" width="454" height="240" viewBox="0 0 454 240">
    <path d="M175 85 A58 58 0 0 0 184 155 M196 168 A58 58 0 0 0 256 168 M268 155 A58 58 0 0 0 278 85" fill="none" stroke="#9f35d8" stroke-width="1.4"/>
    <g fill="#fff" stroke="#9f35d8" stroke-width="1"><circle cx="174" cy="88" r="4"/><circle cx="280" cy="88" r="4"/><circle cx="176" cy="144" r="4"/><circle cx="280" cy="141" r="4"/><circle cx="226" cy="172" r="4"/></g>
    <rect x="194" y="83" width="64" height="64" fill="#9f35d8"/>
  </svg>
  <div class="step" style="left:77px;top:85px"><div class="step__title">Robotic consulting 1</div><p class="step__text">Lorem ipsum dolor sit amet, consectetur adipiscing elit, sed do eiusmod tempor incididunt ut labore et dolore aliqua.</p></div>
  <div class="step" style="left:296px;top:85px"><div class="step__title">Robotic consulting 5</div><p class="step__text">Lorem ipsum dolor sit amet, consectetur adipiscing elit, sed do eiusmod tempor incididunt ut labore et dolore aliqua.</p></div>
  <div class="step" style="left:93px;top:153px"><div class="step__title">Robotic consulting 2</div><p class="step__text">Lorem ipsum dolor sit amet, consectetur adipiscing elit, sed do eiusmod tempor incididunt ut labore et dolore aliqua.</p></div>
  <div class="step" style="left:280px;top:147px"><div class="step__title">Robotic consulting 4</div><p class="step__text">Lorem ipsum dolor sit amet, consectetur adipiscing elit, sed do eiusmod tempor incididunt ut labore et dolore aliqua.</p></div>
  <div class="step" style="left:186px;top:183px"><div class="step__title">Robotic consulting 3</div><p class="step__text">Lorem ipsum dolor sit amet, consectetur adipiscing elit, sed do eiusmod tempor incididunt ut labore et dolore aliqua.</p></div>
  <footer class="footer"><span>05/09/2024</span><span>Copyright © 2024 Novarch. All rights reserved.</span><span>Page: 07</span></footer>
</section>

<!-- Slide 04: presentation list -->
<section class="slide" style="left:35px;top:904px">
  <div class="title center" style="top:32px;font-size:16px">Presentation List</div>
  <p class="para center" style="top:58px;padding:0 48px;text-align:center">Sed ut perspiciatis unde omnis iste natus error sit voluptatem accusantium doloremque laudantium, totam rem ape riam, eaque ipsa quae ab illo inventore veritatis et quasi architecto beatae vitae dicta sunt explicabo.</p>
  <div class="list-row" style="left:38px;top:92px"><span>Robotic consulting 1</span><span style="color:var(--purple)">01</span></div>
  <div class="list-row list-row--accent" style="left:38px;top:129px"><span>Robotic consulting 2</span><span style="color:var(--ink)">02</span></div>
  <div class="list-row" style="left:38px;top:167px"><span>Robotic consulting 3</span><span style="color:var(--purple)">03</span></div>
  <div class="list-row list-row--accent" style="left:38px;top:204px"><span>Robotic consulting 4</span><span style="color:var(--ink)">04</span></div>
  <div class="list-row list-row--accent" style="left:260px;top:92px"><span>Robotic consulting 5</span><span>05</span></div>
  <div class="list-row" style="left:260px;top:129px"><span>Robotic consulting 6</span><span>06</span></div>
  <div class="list-row list-row--accent" style="left:260px;top:167px"><span>Robotic consulting 7</span><span>07</span></div>
  <div class="list-row" style="left:260px;top:204px"><span>Robotic consulting 8</span><span>08</span></div>
  <footer class="footer"><span>05/09/2024</span><span>Copyright © 2024 Novarch. All rights reserved.</span><span>Page: 04</span></footer>
</section>

<!-- Slide 08: thank you -->
<section class="slide slide--cover" style="left:534px;top:905px">
  <div class="brand-mark" style="left:207px;top:28px;width:40px;height:40px"></div>
  <div class="wordmark center" style="top:101px;font-size:16px;padding-left:.22em">NOVARCH</div>
  <div class="abs center" style="top:148px;font-size:22px;font-weight:700">THANK YOU</div>
  <div class="abs center" style="top:178px;font-size:6.6px;line-height:9.5px">Excepteur sint occaecat cupidatat non proident, sunt in culpa<br>deserunt mollit anim id est laborum.</div>
  <footer class="footer"><span>05/09/2024</span><span>Copyright © 2024 Novarch. All rights reserved.</span><span>Page: 08</span></footer>
</section>

</body>
</html>
```